Creative Homepage Design

This is for a security system specifically targeted to:

BANK OWNED PROPERTIES
VACATION HOMES
COMMERCIAL PROPERTIES

The main slides will click into these sections of the website.

The 3 boxes below will link to other sections but should be focused around those topics.

Target Market(s)

BANK OWNED PROPERTIES
VACATION HOMES
COMMERCIAL PROPERTIES

Industry/Entity Type

Security

Requirements
Must have
• must use logo attached
must be designed to the sitemap
must use images that can be purchased from an image database. You will need to provide the detail of where to find the images so that we can purchase.
Nice to have
• Like these designs:
http://www.quorvantelabs.com/
http://www.belmarrowhealth.com/

```html
<!DOCTYPE html>
<html lang="en">
<head>
<meta charset="utf-8">
<title>Kestravo — Property Security</title>
<link rel="stylesheet" href="https://fonts.googleapis.com/css2?family=Open+Sans:wght@400;600;700;800&family=PT+Sans+Narrow:wght@700&family=Arimo:wght@400;700&display=swap">
<style>
:root{
  --page-bg:#323232;
  --red:#d42a1e;
  --red-light:#ee4b3c;
  --red-dark:#a5140c;
  --red-deep:#8e0f08;
  --white:#ffffff;
  --ink:#333333;
  --body-text:#666666;
  --button:#1a1a1a;
}
*{margin:0;padding:0;box-sizing:border-box}
html,body{width:1200px;height:932px;overflow:hidden;background:var(--page-bg)}
.page{position:relative;width:1200px;height:932px}
.site{position:absolute;left:135px;top:41px;width:931px;height:844px;background:var(--white);border-radius:4px;overflow:hidden;box-shadow:0 0 0 2px #1e1e1e}
.header{position:absolute;left:0;top:0;width:931px;height:183px;
  background:radial-gradient(ellipse 420px 160px at 260px 40px,var(--red-light),transparent 75%),
  linear-gradient(100deg,var(--red) 0%,var(--red) 55%,var(--red-dark) 100%)}
.header-arc{position:absolute;left:0;top:0}
.brand{position:absolute;left:33px;top:40px;font-family:"Open Sans",sans-serif;font-weight:800;font-size:50px;letter-spacing:-1px;color:var(--white)}
.utility{position:absolute;right:0;top:6px;height:36px;padding:0 12px 0 14px;background:var(--red-deep);border-radius:6px 0 0 6px;display:flex;align-items:center;gap:6px;font-family:"PT Sans Narrow",sans-serif;font-weight:700;font-size:13.5px;color:var(--white)}
.utility a{color:var(--white);text-decoration:none}
.main-nav{position:absolute;left:236px;top:140px;height:43px;display:flex;align-items:flex-end;font-family:"PT Sans Narrow",sans-serif;font-weight:700;font-size:13.5px}
.main-nav a{color:var(--white);text-decoration:none;padding:0 9px 11px}
.main-nav a.active{background:var(--white);color:#111;border-radius:5px 5px 0 0;padding:16px 16px 11px;margin-right:5px}
.hero{position:absolute;left:0;top:183px;width:931px;height:272px;background:var(--white);overflow:hidden}
.hero-swoosh{position:absolute;left:0;top:0}
.hero-photo{position:absolute;left:0;top:0;width:420px;height:272px;background:linear-gradient(90deg,#e6e6e6 0%,#c9c4c0 40%,#efefef 80%,rgba(255,255,255,0) 100%)}
.hero-line{position:absolute;font-family:"Open Sans",sans-serif;font-weight:700;color:var(--ink);line-height:1;white-space:nowrap}
.hero-line.task{left:439px;top:65px;font-size:54px;letter-spacing:-1.5px}
.hero-line.task small{font-size:27px;letter-spacing:0}
.hero-line.make{left:561px;top:113px;font-size:25px;letter-spacing:-0.3px}
.hero-line.make .dot{display:inline-block;width:15px;height:15px;border-radius:50%;background:var(--red);vertical-align:-1px;margin:0 1px}
.hero-line.notice{left:446px;top:110px;font-size:78px;letter-spacing:-2.5px}
.hero-cta{position:absolute;left:738px;top:190px;padding:3px 10px 5px;background:var(--red);color:var(--white);border-radius:5px;font-family:"Open Sans",sans-serif;font-weight:700;font-size:14px;text-decoration:none}
.hero-rule{position:absolute;left:0;top:455px;width:931px;height:3px;background:#2b2b2b}
.feature{position:absolute;top:480px;width:285px}
.feature-title{height:53px;border-radius:5px 5px 2px 2px;padding:22px 10px 0;font-family:"Open Sans",sans-serif;font-weight:400;font-size:15.5px;color:var(--white);
  background:linear-gradient(165deg,var(--red-light) 0%,var(--red) 30%,var(--red-dark) 100%)}
.feature-photo{margin-top:5px;height:100px;border-radius:5px}
.feature-text{margin-top:14px;padding-left:6px;width:268px;font-family:"Arimo",sans-serif;font-size:11.5px;line-height:20px;color:var(--body-text)}
.feature-more{display:inline-block;margin:10px 0 0 4px;padding:3px 7px 4px;background:var(--button);border-radius:4px;border:1px solid #555;color:var(--white);font-family:"Arimo",sans-serif;font-weight:700;font-size:12.5px;text-decoration:none}
</style>
</head>
<body>
<div class="page">
  <div class="site">
    <header class="header">
      <svg class="header-arc" width="931" height="183" viewBox="0 0 931 183">
        <path d="M560 0 C690 40 740 120 760 183 L931 183 L931 0 Z" fill="#a5140c" opacity=".35"/>
      </svg>
      <div class="brand">KESTRAVO</div>
      <nav class="utility"><a href="#">HOME</a>|<a href="#">ABOUT US</a>|<a href="#">CUSTOMER LOGIN</a></nav>
      <nav class="main-nav">
        <a class="active" href="#">BANK OWNED PROPERTIES</a>
        <a href="#">VACATION HOMES</a>
        <a href="#">COMMERCIAL PROPERTIES</a>
        <a href="#">HOW IT WORKS</a>
        <a href="#">SUPPORT</a>
        <a href="#">CONTACT US</a>
      </nav>
    </header>
    <section class="hero">
      <svg class="hero-swoosh" width="931" height="272" viewBox="0 0 931 272">
        <defs><linearGradient id="sw" x1="0" x2="1"><stop offset="0" stop-color="#fbe3e1" stop-opacity="0"/><stop offset="1" stop-color="#f3b9b3"/></linearGradient></defs>
        <path d="M420 272 C560 170 760 90 931 60 L931 100 C780 130 600 200 500 272 Z" fill="url(#sw)" opacity=".6"/>
        <path d="M600 0 C720 30 860 20 931 0 L931 30 C840 55 720 50 600 0 Z" fill="url(#sw)" opacity=".4"/>
      </svg>
      <div class="hero-photo" role="img" aria-label="Smiling woman holding a small model house in her hands"></div>
      <h1 class="hero-headline">
        <span class="hero-line task">Our task <small>is</small></span>
        <span class="hero-line notice">noticeable</span>
        <span class="hero-line make">t<span class="dot"></span> make you</span>
      </h1>
      <a class="hero-cta" href="#">read more</a>
    </section>
    <div class="hero-rule"></div>

    <article class="feature" style="left:19px">
      <h2 class="feature-title">PIECE OF MIND</h2>
      <div class="feature-photo" role="img" aria-label="Young couple moving into a new house" style="background:linear-gradient(90deg,#d8cbbb,#a89886 50%,#e0dcd6)"></div>
      <p class="feature-text">Lorem ipsum dolor sit amet, consectetur adipiscing elit. Phasellus velit. Aliquam auctor sapien vitae erat. Aliquam vel mi.&nbsp; Class aptent taciti sociosqu ad litora&nbsp; torquent per conubia nostra. nec, suscipit id, congue non.</p>
      <a class="feature-more" href="#">Read More »</a>
    </article>
    <article class="feature" style="left:322px">
      <h2 class="feature-title">SECURITY FROM $PRICE</h2>
      <div class="feature-photo" role="img" aria-label="Hand holding house keys in front of a home under blue sky" style="background:linear-gradient(90deg,#c9b08a,#2f7fd0 45%,#1a6fd6)"></div>
      <p class="feature-text">Lorem ipsum dolor sit amet, consectetur adipiscing elit. Phasellus velit. Aliquam auctor sapien vitae erat. Aliquam vel mi.&nbsp; Class aptent taciti sociosqu ad litora&nbsp; torquent per conubia nostra. nec, suscipit id, congue non.</p>
      <a class="feature-more" href="#">Read More »</a>
    </article>
    <article class="feature" style="left:626px">
      <h2 class="feature-title">GET STARTED</h2>
      <div class="feature-photo" role="img" aria-label="Businessmen at a starting line outdoors" style="background:linear-gradient(180deg,#5f9fd8,#bcd6ee 55%,#7c8a70)"></div>
      <p class="feature-text">Lorem ipsum dolor sit amet, consectetur adipiscing elit. Phasellus velit. Aliquam auctor sapien vitae erat. Aliquam vel mi.&nbsp; Class aptent taciti sociosqu ad litora&nbsp; torquent per conubia nostra. nec, suscipit id, congue non.</p>
      <a class="feature-more" href="#">Read More »</a>
    </article>
  </div>
</div>
</body>
</html>
```